Accounting Business needs double sided DL flyer design

We need a double sided DL flyer designed,
Front side with logo, web address and our short intro.
Backside to have a list of services.
Our colours are blue and a concrete grey colour. Look at our website for a feel for our colour scheme.
www.lanternwellgroup.com.au
I have included the pic from our website to possibly use but we are also open to new creative ideas.
Target Market(s)
Our target market are proactive business owners, particularly in the wine and hospitality industry.
Industry/Entity Type
Business
Look and feel

```html
<!DOCTYPE html>
<html lang="en">
<head>
<meta charset="utf-8">
<title>Lanternwell Group – DL Flyer</title>
<link rel="stylesheet" href="https://fonts.googleapis.com/css2?family=Oswald:wght@400;500;700&family=Roboto+Condensed:wght@400;700&display=swap">
<style>
:root{
  --blue:#17468a;
  --blue-dark:#123a74;
  --ink:#2b2b2b;
  --charcoal:#333333;
  --concrete:#c9cdd1;
  --concrete-light:#eef0f1;
  --page:#e7e7e7;
  --white:#ffffff;
}
*{box-sizing:border-box;margin:0;padding:0}
html,body{width:1200px;height:1200px;overflow:hidden;background:var(--page)}
.canvas{position:relative;width:1200px;height:1200px}
.flyer{position:absolute;top:63px;width:522px;height:1073px;background:var(--white);overflow:hidden;box-shadow:0 2px 6px rgba(0,0,0,.25)}
.flyer--front{left:57px;background:linear-gradient(180deg,#fafafa 0%,#eef0f1 45%,#dfe2e4 100%)}
.flyer--back{left:621px}

.brand{position:absolute;display:flex;align-items:center;gap:12px}
.brand__mark{background:var(--blue);flex:none}
.brand__name{font-family:"Oswald",sans-serif;font-weight:700;color:var(--blue);letter-spacing:.06em;line-height:1}
.brand__line{font-family:"Roboto Condensed",sans-serif;color:var(--blue);letter-spacing:.3em;margin-top:6px;border-top:1.5px solid var(--blue);padding-top:6px}

.flyer--front .brand{left:50px;top:85px}
.flyer--front .brand__mark{width:58px;height:58px}
.flyer--front .brand__name{font-size:36px}
.flyer--front .brand__line{font-size:11.5px}

.headline{position:absolute;left:46px;top:293px;width:440px;height:245px;overflow:visible}
.headline text{font-family:"Oswald",sans-serif}
.headline__a{font-size:79px;font-weight:400;fill:var(--ink)}
.headline__b{font-size:65px;font-weight:700;fill:var(--blue)}
.headline__c{font-size:50px;font-weight:700;fill:var(--ink)}
.headline__d{font-size:50px;font-weight:700;fill:var(--blue)}

.stairs-photo{position:absolute;left:0;top:560px;width:522px;height:380px;background:linear-gradient(160deg,rgba(255,255,255,0) 0%,#cfd3d6 40%,#a9afb4 100%)}

.front-band{position:absolute;left:0;top:880px;width:522px;height:140px;background:var(--blue);border-top:6px solid var(--blue);box-shadow:inset 0 6px 0 var(--white)}
.front-band::after{content:"";position:absolute;left:0;right:0;bottom:0;height:6px;background:var(--white)}
.phone{position:absolute;display:flex;align-items:center;justify-content:center;gap:18px;color:var(--white);font-family:"Oswald",sans-serif;font-weight:500}
.front-band .phone{left:0;right:0;top:36px;font-size:44px}
.front-web{position:absolute;left:0;top:1020px;width:522px;height:53px;background:var(--charcoal);color:var(--white);font-family:"Roboto Condensed",sans-serif;font-size:21px;letter-spacing:.17em;text-align:center;line-height:53px}

.services-head{position:absolute;left:0;top:0;width:522px;height:74px;background:var(--blue);color:var(--white);font-family:"Oswald",sans-serif;font-weight:500;font-size:33px;text-align:center;line-height:74px;letter-spacing:.02em}
.service{position:absolute;width:219px;text-align:center;font-family:"Roboto Condensed",sans-serif;font-size:17px;color:var(--ink);line-height:1.2}
.service__photo{display:block;width:219px;height:80px;border:1.5px solid var(--blue);margin-bottom:8px}

.flyer--back .brand{left:110px;top:883px;gap:10px}
.flyer--back .brand__mark{width:44px;height:44px}
.flyer--back .brand__name{font-size:23px}
.flyer--back .brand__line{font-size:8px;margin-top:4px;padding-top:4px}

.back-band{position:absolute;left:0;top:955px;width:522px;height:118px;background:var(--blue);border-top:4px solid var(--charcoal);box-shadow:inset 0 4px 0 var(--white)}
.back-band .phone{left:0;right:0;top:22px;font-size:36px;gap:14px}
.back-web{position:absolute;left:0;right:0;top:72px;text-align:center;color:var(--white);font-family:"Roboto Condensed",sans-serif;font-size:23px}
</style>
</head>
<body>
<div class="canvas">

  <section class="flyer flyer--front">
    <div class="brand">
      <div class="brand__mark"></div>
      <div>
        <div class="brand__name">LANTERNWELL GROUP</div>
        <div class="brand__line">BUSINESS ADVISORS &amp; ACCOUNTANTS</div>
      </div>
    </div>

    <svg class="headline" viewBox="0 0 440 245" role="heading" aria-level="1" aria-label="A guiding hand, a voice of reason, a partner you can trust for success">
      <text class="headline__a" x="0" y="68" textLength="428" lengthAdjust="spacingAndGlyphs">A GUIDING HAND</text>
      <text class="headline__b" x="2" y="130" textLength="424" lengthAdjust="spacingAndGlyphs">A VOICE OF REASON</text>
      <text class="headline__c" x="0" y="184" textLength="430" lengthAdjust="spacingAndGlyphs">A PARTNER YOU CAN TRUST</text>
      <text class="headline__d" x="0" y="237" textLength="426" lengthAdjust="spacing">FOR SUCCESS</text>
    </svg>

    <div class="stairs-photo" role="img" aria-label="White concrete staircase rising along a grey wall in soft light"></div>

    <div class="front-band">
      <div class="phone">
        <svg width="68" height="46" viewBox="0 0 68 46" aria-hidden="true">
          <path d="M6 14c10-10 38-10 48 0l-4 8-9-3v-5c-7-2-15-2-22 0v5l-9 3z" fill="#fff"/>
          <rect x="12" y="22" width="36" height="22" rx="6" fill="#fff"/>
          <circle cx="30" cy="33" r="7" fill="none" stroke="#17468a" stroke-width="3"/>
          <path d="M56 8q5 6 0 12M61 4q8 10 0 20" stroke="#fff" stroke-width="2.5" fill="none"/>
        </svg>
        <span>0491 570 118</span>
      </div>
    </div>
    <div class="front-web">www.lanternwellgroup.com.au</div>
  </section>

  <section class="flyer flyer--back">
    <h2 class="services-head">OUR SERVICES</h2>

    <div class="service" style="left:28px;top:93px"><span class="service__photo" role="img" aria-label="Hands working a calculator over tax paperwork" style="background:linear-gradient(135deg,#e9e8e4,#8c8f96)"></span>Taxation Compliance</div>
    <div class="service" style="left:272px;top:93px"><span class="service__photo" role="img" aria-label="Financial chart on a dark blue market screen" style="background:linear-gradient(135deg,#0f2446,#2f5d9a)"></span>Financial &amp; Management<br>Reporting</div>

    <div class="service" style="left:28px;top:225px"><span class="service__photo" role="img" aria-label="Beach chair by a sunlit sea" style="background:linear-gradient(180deg,#c9dbe8,#8fa7b4 55%,#e2ddd2)"></span>Self-Managed Superannuation</div>
    <div class="service" style="left:272px;top:225px"><span class="service__photo" role="img" aria-label="Hands typing on a laptop beside a coffee cup" style="background:linear-gradient(135deg,#2b5a86,#8ab3c8)"></span>Virtual CFO</div>

    <div class="service" style="left:28px;top:347px"><span class="service__photo" role="img" aria-label="Sketched organisation flowchart on paper" style="background:linear-gradient(135deg,#eef2f6,#c5d0db)"></span>Business Planning</div>
    <div class="service" style="left:272px;top:347px"><span class="service__photo" role="img" aria-label="Motorcycle speedometer dashboard" style="background:linear-gradient(135deg,#1c1e22,#5a6068)"></span>KPIs &amp; Performance Monitoring</div>

    <div class="service" style="left:28px;top:475px"><span class="service__photo" role="img" aria-label="Businessman silhouette at a tall office window" style="background:linear-gradient(180deg,#dfe5ea,#9aa6b0)"></span>Succession Planning</div>
    <div class="service" style="left:272px;top:475px"><span class="service__photo" role="img" aria-label="Pebble beach stretching to the sea" style="background:linear-gradient(180deg,#b9c2c8,#6d6a66)"></span>Estate Planning</div>

    <div class="service" style="left:28px;top:598px"><span class="service__photo" role="img" aria-label="Cables connecting to a white cloud shape" style="background:linear-gradient(135deg,#cfe3ee,#9cc3d8)"></span>Cloud Solutions</div>
    <div class="service" style="left:272px;top:598px"><span class="service__photo" role="img" aria-label="Team of hands stacked together" style="background:linear-gradient(135deg,#6e7a5e,#c19a84)"></span>Business Support Services</div>

    <div class="service" style="left:152px;top:728px"><span class="service__photo" role="img" aria-label="Grapes being stirred in a wine barrel" style="background:linear-gradient(135deg,#3a1f24,#7d3a55)"></span>The Wine Industry</div>

    <div class="brand">
      <div class="brand__mark"></div>
      <div>
        <div class="brand__name">LANTERNWELL GROUP</div>
        <div class="brand__line">BUSINESS ADVISORS &amp; ACCOUNTANTS</div>
      </div>
    </div>

    <div class="back-band">
      <div class="phone">
        <svg width="56" height="38" viewBox="0 0 68 46" aria-hidden="true">
          <path d="M6 14c10-10 38-10 48 0l-4 8-9-3v-5c-7-2-15-2-22 0v5l-9 3z" fill="#fff"/>
          <rect x="12" y="22" width="36" height="22" rx="6" fill="#fff"/>
          <circle cx="30" cy="33" r="7" fill="none" stroke="#17468a" stroke-width="3"/>
          <path d="M56 8q5 6 0 12M61 4q8 10 0 20" stroke="#fff" stroke-width="2.5" fill="none"/>
        </svg>
        <span>0491 570 118</span>
      </div>
      <div class="back-web">www.lanternwellgroup.com.au</div>
    </div>
  </section>

</div>
</body>
</html>
```